Brisk Bookings needs a New Home page

We provide online appointment scheduling. There are many schedulers out there. Ours is unique because the scheduler is shown in one compact view that can be easily incorporated into the customer's website or Chatterbay page. Whether our customer is a solo hair-stylist or a large testing center with hundreds of testing seats at multiple locations, our customer still gets the same easy-to-use, one-page scheduling experience.

Our current home page, briskbookings.example, feels cluttered and outdated. We want something more modern and minimal.

Here are web pages we like:
artmosaic.example
tillquay.example
ruvel.example

We are not unhappy with the current logo or color scheme.

Need very clear call(s) to action (i.e. sign up for trial, schedule a demo).
Design needs to look good on devices of varying size.

Here are some ideas:
“Simple Online Scheduling” - Simple, compact design, easy-to-use & powerful, time-saving, chaos-taming, affordable, one page scheduling
“Stay in touch” - Basic email confirmations, reminders or targeted email notifications for follow-ups, no shows and more
“Multiple locations? No problem” - Schedule for multiple locations on one scheduler -
“Resource Pools” - Batting cages, clerks at the DMV, computers in a lab, pilates reformer machines
“Go Social” - Scheduling for Chatterbay and mobile devices
“Visual Reporting” - Reports
“Trusted” - Testimonials, reliable since 2005, etc.
List of industries (with links to industry-specific pages)

Ultimately want to redevelop the full site.
Updates

Reason: Please do not submit any new designs. We are now just wrapping up polling and discussing details. Thank you to all designers who have submitted. We feel lucky to get to chose from many great designs.

Target Market(s)

Audience is very broad including solo entrepreneurs (massage therapist, accountants, lawyers), educational institutions (elementary schools, university departments, advisers, testing centers), health care providers and screening services, to government.

Industry/Entity Type

Online

Requirements
Must have
• Call(s) to action, i.e. sign up for trial, schedule a demo.
• Look good on devices of different sizes.

```html
<!DOCTYPE html>
<html lang="en">
<head>
<meta charset="utf-8">
<title>Brisk Bookings – Easy One Page Scheduling</title>
<link href="https://fonts.googleapis.com/css2?family=Quicksand:wght@300;400;500;700&family=Open+Sans:wght@400;600;700&display=swap" rel="stylesheet">
<style>
:root{
  --green:#8cbf26;
  --green-dark:#6f9c17;
  --orange:#f0562a;
  --red:#e4402a;
  --text:#5b5b5b;
  --heading:#2e2e2e;
  --muted:#8a8a8a;
  --link-blue:#5b6d8f;
  --page:#f1f2f4;
  --band:#e4e7ed;
  --white:#ffffff;
}
*{margin:0;padding:0;box-sizing:border-box}
html,body{width:1200px;height:2812px;overflow:hidden}
body{position:relative;background:var(--white);font-family:"Open Sans",sans-serif;color:var(--text)}
.abs{position:absolute}
a{text-decoration:none;color:inherit}

/* nav */
.topbar{left:0;top:0;width:1200px;height:61px;background:var(--white)}
.brand{left:129px;top:14px;font-family:"Quicksand",sans-serif;font-weight:700;font-size:30px;color:var(--green);display:flex;align-items:center;gap:8px}
.brand .dot{width:12px;height:12px;border-radius:50%;background:var(--orange)}
.nav{left:445px;top:0;display:flex;height:61px;font-family:"Quicksand",sans-serif;font-size:16px;color:#555}
.nav a{display:flex;align-items:center;padding:0 14px}
.nav a.active{background:var(--green);color:var(--white);width:71px;justify-content:center;padding:0}
.login{left:1008px;top:0;width:70px;height:23px;background:var(--orange);color:var(--white);font-size:14px;font-weight:600;text-align:center;line-height:23px}

/* hero */
.hero{left:0;top:61px;width:1200px;height:469px;background:radial-gradient(ellipse at 55% 30%,#a89580 0%,#85715e 45%,#5d4e41 100%)}
.hero-title{left:136px;top:92px;font-family:"Quicksand",sans-serif;font-weight:300;font-size:60px;letter-spacing:2px;color:var(--white)}
.hero-sub{left:136px;top:213px;font-family:"Quicksand",sans-serif;font-weight:700;font-size:23px;line-height:29px;color:var(--white)}
.hero-sub .num{display:inline-block;width:28px;height:28px;border:2px solid var(--white);border-radius:50%;text-align:center;line-height:24px;font-size:20px}
.steps{left:136px;top:274px;list-style:none;font-family:"Quicksand",sans-serif;font-size:25px;color:var(--white)}
.steps li{height:33px;display:flex;align-items:center;gap:16px}
.steps svg{width:20px;height:20px}
.hero-cta{left:164px;top:459px;width:270px;height:45px;background:var(--green);color:var(--white);font-family:"Quicksand",sans-serif;font-size:23px;font-weight:500;text-align:center;line-height:45px;border-radius:3px}
.device-laptop{left:516px;top:234px;width:422px;height:286px;background:linear-gradient(#2a2a2a 0 6%,#eef1e6 6% 88%,#c9cbcf 88%);border-radius:10px 10px 4px 4px}
.device-phone{left:949px;top:281px;width:117px;height:234px;background:linear-gradient(#1e1e1e 0 12%,#e9eaec 12% 88%,#1e1e1e 88%);border-radius:14px}

/* tabs */
.tabs{left:0;top:530px;width:1200px;height:75px;background:var(--white);display:flex;justify-content:center;gap:40px;align-items:center;font-family:"Quicksand",sans-serif;font-size:17px;letter-spacing:1px;color:#666;padding-right:20px}
.tabs .on{color:var(--orange)}

/* features */
.features{left:0;top:605px;width:1200px;height:1411px;background:linear-gradient(#f7f7f8,#eceef2)}
.feat-img{border-radius:6px}
.feat-title{font-family:"Quicksand",sans-serif;font-weight:400;font-size:40px;color:var(--heading);letter-spacing:1px}
.feat-text{font-family:"Quicksand",sans-serif;font-size:15px;line-height:24px;color:var(--text);width:630px}
.feat-link{font-family:"Quicksand",sans-serif;font-size:23px;color:var(--green)}
.waiting{left:0;top:1864px;width:1200px;text-align:center;font-family:"Quicksand",sans-serif;font-size:38px;color:var(--heading)}
.demo-btn{left:483px;top:1943px;width:232px;height:38px;background:var(--green);color:var(--white);font-family:"Open Sans",sans-serif;font-weight:600;font-size:17px;text-align:center;line-height:38px;border-radius:3px;border-bottom:3px solid var(--green-dark)}

/* clients */
.who{left:0;top:2066px;width:1200px;text-align:center;font-weight:700;font-size:26px;color:var(--red)}
.who .name{color:var(--green);font-family:"Quicksand",sans-serif}
.client{top:2150px;font-family:"Open Sans",sans-serif;font-weight:700;font-size:19px;color:#3d4a66;text-align:center}
.testimonials{left:815px;top:2231px;width:209px;text-align:right;font-size:15px;color:var(--red);text-decoration:underline}

/* industries */
.industries{left:0;top:2285px;width:1200px;height:305px;background:var(--band)}
.ind-title{left:0;top:2308px;width:1200px;text-align:center;font-family:"Quicksand",sans-serif;font-size:36px;color:var(--heading);letter-spacing:1px}
.ind-col{top:2392px;list-style:none;font-size:16px;line-height:22px;color:var(--link-blue)}
.ind-col li{text-decoration:underline}
.full-list{left:0;top:2562px;width:1200px;text-align:center;font-family:"Quicksand",sans-serif;font-size:18px;color:var(--green);text-decoration:underline}

/* footer */
.foot-col{top:2604px;width:330px;font-size:12.5px;line-height:17px;color:#444}
.foot-col h4{font-size:14px;color:var(--red);font-weight:600;margin-bottom:12px}
.foot-col p{margin-bottom:10px}
.foot-col ul{list-style:none}
.foot-col li{display:flex;gap:8px;margin-bottom:8px}
.foot-col li svg{flex:none;width:13px;height:13px;margin-top:2px}
.foot-rule{left:117px;top:2778px;width:966px;height:1px;background:#d6d6d6}
.foot-mark{left:589px;top:2765px;width:22px;height:22px;border-radius:50%;border:2px solid var(--orange);background:var(--white)}
.copy{top:2793px;font-size:12px;color:#555}
</style>
</head>
<body>

<header class="abs topbar">
  <div class="abs brand"><span class="dot"></span>Brisk Bookings</div>
  <nav class="abs nav">
    <a class="active">Home</a><a>See it work</a><a>Who it's for</a><a>Our Scheduler</a><a>FREE Trial</a><a>Dig in</a><a>About Us</a>
  </nav>
  <a class="abs login">Login</a>
</header>

<section class="abs hero" role="img" aria-label="Soft blurred brown backdrop with a faint dotted world map"></section>
<h1 class="abs hero-title">Easy One Page Scheduling</h1>
<p class="abs hero-sub">Schedule your appointments<br>in just <span class="num">5</span> steps</p>
<ul class="abs steps">
  <li><svg viewBox="0 0 20 20"><path d="M2 11l5 5 11-12" fill="none" stroke="#fff" stroke-width="3"/></svg>Select a date</li>
  <li><svg viewBox="0 0 20 20"><path d="M2 11l5 5 11-12" fill="none" stroke="#fff" stroke-width="3"/></svg>Select a service</li>
  <li><svg viewBox="0 0 20 20"><path d="M2 11l5 5 11-12" fill="none" stroke="#fff" stroke-width="3"/></svg>Select an opening</li>
  <li><svg viewBox="0 0 20 20"><path d="M2 11l5 5 11-12" fill="none" stroke="#fff" stroke-width="3"/></svg>Enter contact information</li>
  <li><svg viewBox="0 0 20 20"><path d="M2 11l5 5 11-12" fill="none" stroke="#fff" stroke-width="3"/></svg>Confirm appointment</li>
</ul>
<a class="abs hero-cta">Try it now for Free!</a>
<div class="abs device-laptop" role="img" aria-label="Laptop showing the one page scheduler screen"></div>
<div class="abs device-phone" role="img" aria-label="Smartphone showing the scheduler"></div>

<nav class="abs tabs"><span class="on">KEY FEATURES</span><span>WHO USES BRISKBOOKINGS</span><span>INDUSTRIES</span></nav>

<section class="abs features"></section>

<div class="abs feat-img" style="left:152px;top:633px;width:211px;height:211px;background:linear-gradient(135deg,#2f5fd0,#0e2a8c)" role="img" aria-label="Blue rising line chart on a glossy panel"></div>
<h2 class="abs feat-title" style="left:422px;top:658px">Save Time, Simplify, It's Affordable</h2>
<p class="abs feat-text" style="left:424px;top:720px">Short sentence describing the features behind the application. Its length should be as long as this text runs, 2-3 lines at most.</p>
<a class="abs feat-link" style="left:851px;top:775px">See how it works ›</a>

<h2 class="abs feat-title" style="left:129px;top:944px">Go Social!</h2>
<p class="abs feat-text" style="left:129px;top:1013px">Scheduling for Chatterbay and mobile devices. Short sentence describing this feature behind the application. Its length should be as long as this text runs, 2-3 lines at most.</p>
<a class="abs feat-link" style="left:129px;top:1087px">Watch it in action ›</a>
<div class="abs feat-img" style="left:785px;top:1003px;width:246px;height:134px;background:linear-gradient(#1b1b1b 0 8%,#dfe5f0 8% 92%,#1b1b1b 92%);border-radius:12px" role="img" aria-label="Tablet showing a social page with the scheduler"></div>

<div class="abs feat-img" style="left:152px;top:1219px;width:223px;height:223px;background:linear-gradient(#f4f4f4,#d9d9d9)" role="img" aria-label="Envelope holding a targeted email notification card"></div>
<h2 class="abs feat-title" style="left:417px;top:1279px">Stay in touch.</h2>
<p class="abs feat-text" style="left:417px;top:1341px;width:660px">Basic email confirmations, reminders or targeted email notifications for follow-ups. Same as before. 2-3 lines at most in order for design to be coherent.</p>
<a class="abs feat-link" style="left:826px;top:1410px">Try it today for Free ›</a>

<h2 class="abs feat-title" style="left:129px;top:1623px">Multiple Locations?</h2>
<p class="abs feat-text" style="left:129px;top:1686px">No problem! Short sentence describing this feature behind the application. Its length should be as long as this text runs, 2-3 lines at most.</p>
<a class="abs feat-link" style="left:129px;top:1745px">Find out more ›</a>
<div class="abs feat-img" style="left:781px;top:1613px;width:250px;height:192px;background:linear-gradient(135deg,#e8e4d8,#c9c4b4)" role="img" aria-label="Folded street map with location pins"></div>

<h2 class="abs waiting">What are you waiting for?</h2>
<a class="abs demo-btn">Schedule a demo today</a>
<svg class="abs" style="left:0;top:2010px" width="1200" height="44" viewBox="0 0 1200 44">
  <path d="M0 0H1200V6H632L600 40 568 6H0Z" fill="#eceef2"/>
</svg>

<h2 class="abs who">Who uses <span class="name">Brisk Bookings</span></h2>
<div class="abs client" style="left:170px;width:150px">Harbor Online<br>Academy</div>
<div class="abs client" style="left:385px;width:195px;top:2160px">Westmere University</div>
<div class="abs client" style="left:640px;width:150px">Teach Forward<br>Corps</div>
<div class="abs client" style="left:850px;width:175px;font-size:15px;top:2156px">Bright Path Learning</div>
<a class="abs testimonials">Read all the testimonials ›</a>

<section class="abs industries"></section>
<h2 class="abs ind-title">Scheduling online appointments for:</h2>
<svg class="abs" style="left:285px;top:2388px" width="630" height="160" viewBox="0 0 630 160">
  <path d="M36 4C14 4 20 30 20 60C20 74 14 80 4 80C14 80 20 86 20 100C20 130 14 156 36 156" fill="none" stroke="#e4402a" stroke-width="6" stroke-linecap="round"/>
  <path d="M594 4C616 4 610 30 610 60C610 74 616 80 626 80C616 80 610 86 610 100C610 130 616 156 594 156" fill="none" stroke="#e4402a" stroke-width="6" stroke-linecap="round"/>
</svg>
<ul class="abs ind-col" style="left:372px"><li>accounting</li><li>acupuncture</li><li>automotive</li><li>advising</li><li>barber</li><li>chiropractic</li><li>counseling</li></ul>
<ul class="abs ind-col" style="left:551px"><li>dental</li><li>education</li><li>fitness</li><li>government</li><li>hair removal</li><li>health</li><li>home services</li></ul>
<ul class="abs ind-col" style="left:720px"><li>homeopathy</li><li>interviewing</li><li>laser equipment</li><li>legal</li><li>martial arts</li><li>massage</li><li>medical</li></ul>
<a class="abs full-list">See the full list ›</a>

<footer>
  <div class="abs foot-col" style="left:117px">
    <h4>Easy to Use.</h4>
    <p>Our appointment scheduler is a rich internet application (RIA). Updates occur quickly on a single compact page making it easy for clients to shop for an ideal opening.</p>
    <p>That is important, especially when your appointment calendar is filling up and availability is limited.</p>
  </div>
  <div class="abs foot-col" style="left:497px">
    <h4>Affordable.</h4>
    <p>Online appointment scheduling starts at just $10/month with the Solo Plan. All plans offer:</p>
    <ul>
      <li><svg viewBox="0 0 13 13"><path d="M1 7l4 4 7-10" fill="none" stroke="#e4402a" stroke-width="2.4"/></svg>Unlimited appointments and unlimited users.</li>
      <li><svg viewBox="0 0 13 13"><path d="M1 7l4 4 7-10" fill="none" stroke="#e4402a" stroke-width="2.4"/></svg>No sneaky charges for high appointment scheduling volume or additional logins.</li>
    </ul>
  </div>
  <div class="abs foot-col" style="left:816px">
    <h4>Powerful.</h4>
    <p>The online appointment scheduler scales up to meet your growing business needs. Try our online scheduling demos to see how we can handle:</p>
    <ul>
      <li><svg viewBox="0 0 13 13"><path d="M1 7l4 4 7-10" fill="none" stroke="#e4402a" stroke-width="2.4"/></svg>Many schedules.</li>
      <li><svg viewBox="0 0 13 13"><path d="M1 7l4 4 7-10" fill="none" stroke="#e4402a" stroke-width="2.4"/></svg>Complex service menus.</li>
      <li><svg viewBox="0 0 13 13"><path d="M1 7l4 4 7-10" fill="none" stroke="#e4402a" stroke-width="2.4"/></svg>Multiple locations</li>
    </ul>
  </div>
  <div class="abs foot-rule"></div>
  <div class="abs foot-mark"></div>
  <p class="abs copy" style="left:230px">Copyright 2013 Brisk Bookings</p>
  <p class="abs copy" style="left:621px">Copyright | Privacy and Billing Policies | Terms and Conditions</p>
</footer>

</body>
</html>
```